Energieberater sucht Flyer-Design
Zielgruppe
Ich bin Energieberater, habe mich vor kurzem selbstständig gemacht und möchte nun meine Bekanntheit steigern. Meine Zielgruppe sind Immobilieneigentümer sowie Immobiliensuchende, welchen ich eine fundierte Energieberatung mit Sanierungskonzepten sowie die Erstellung von Energieausweisen bieten kann.
Aufgabenstellung
Ich benötige einen Flyer, welchen ich regional verteilen möchte. Der Flyer soll quadratisch (148 x 148) erstellt werden.
Der Flyer sollte mein Logo, meine Kontaktdaten, die unten aufgeführten Dienstleistungen sowie einen Gutschein enthalten und insbesondere der Bekanntheits-/Imagesteigerung dienen.
Vorhandene Punkte sollen sein:
- Erstellung von Energieausweisen für Vermietung und Verkauf
- Energieberatung
- Sanierungs- und Modernisierungskonzepte
- Fördermittelberatung
Der Flyer soll die Möglichkeit bieten, am Rand abgeschnitten zu werden. Dort soll ein Gutschein aufgeführt werden mit 25 € Rabatt für einen Energieausweis.
Meine Kontaktdaten können Sie der angehängten Visitenkarte entnehmen.

```html
<!DOCTYPE html>
<html lang="de">
<head>
<meta charset="utf-8">
<title>Flyer Energieberatung Wendel</title>
<link href="https://fonts.googleapis.com/css2?family=Quicksand:wght@500;600;700&family=Oswald:wght@600&family=Montserrat:wght@700;800&display=swap" rel="stylesheet">
<style>
  :root{
    --stage:#424242;
    --teal:#217a97;
    --olive:#a5a32c;
    --slate:#707070;
    --gold:#e3ac2a;
    --white:#ffffff;
    --yellow:#e8c51d;
    --orange:#e9841a;
    --red:#d81f1f;
    --lime:#a4b52a;
  }
  *{box-sizing:border-box;margin:0;padding:0}
  html,body{width:1200px;height:623px;overflow:hidden;background:var(--stage)}
  body{position:relative;font-family:"Quicksand",sans-serif}

  .side{position:absolute;overflow:hidden}
  .side--front{left:41px;top:38px;width:537px;height:537px;background:var(--white)}
  .side--back{left:615px;top:38px;width:538px;height:539px;background:var(--white)}

  /* front */
  .brand{position:absolute;left:32px;top:82px;display:flex;align-items:center;gap:12px}
  .brand__mark{width:22px;height:22px;background:var(--teal)}
  .brand__name{color:var(--teal);font-weight:700;font-size:26px;letter-spacing:.5px}

  .hero{position:absolute;left:0;top:145px;width:537px;height:258px;
    background:linear-gradient(135deg,#bcd0e3 0%,#dcdfd2 55%,#c6d3a4 100%)}
  .hero__corner{position:absolute;left:0;top:145px;width:537px;height:258px}

  .services{position:absolute;left:30px;top:430px;width:480px;height:90px}
  .service{position:absolute;display:flex;gap:9px;color:var(--teal);font-weight:700;font-size:15.5px;line-height:16px}
  .service::before{content:"";flex:none;width:9px;height:9px;margin-top:4px;background:var(--dot)}
  .service--a{left:0;top:2px;--dot:var(--yellow)}
  .service--b{left:276px;top:0;--dot:var(--red)}
  .service--c{left:0;top:49px;--dot:var(--orange)}
  .service--d{left:276px;top:46px;--dot:var(--lime)}

  .stripes{position:absolute;left:29px;top:508px;width:478px}
  .stripes span{display:block;height:2px;margin-bottom:3px}

  /* back */
  .intro{position:absolute;left:0;top:0;width:538px;height:229px;background:var(--teal);
    padding:36px 30px 0 34px;color:var(--white);font-size:12.1px;line-height:14.2px;font-weight:500;text-align:justify}
  .intro p{margin-bottom:14px}

  .contact-band{position:absolute;left:0;top:233px;width:538px;height:145px;display:flex}
  .contact-band__name{width:218px;background:var(--olive);color:var(--white);padding:54px 0 0 33px}
  .contact-band__name small{display:block;font-size:15px;font-weight:500}
  .contact-band__name strong{display:block;font-size:22px;font-weight:700;margin-top:3px}
  .contact-band__data{flex:1;background:var(--slate);color:var(--white);font-weight:700;font-size:15px;line-height:18px;padding:33px 0 0 22px}
  .contact-line{display:flex;gap:8px;align-items:flex-start}
  .contact-line svg{flex:none;width:12px;height:12px;margin-top:3px;fill:var(--white)}
  .contact-line + .contact-line{margin-top:17px}
  .contact-line--mail{margin-top:1px !important}

  .cut-line{position:absolute;left:0;top:387px;width:538px;border-top:2px dotted #555}

  .coupon{position:absolute;left:0;top:390px;width:538px;height:149px;background:linear-gradient(180deg,var(--white),#e4e4e4)}
  .coupon__brand{position:absolute;left:35px;top:28px;display:flex;align-items:center;gap:6px}
  .coupon__brand .brand__mark{width:9px;height:9px}
  .coupon__brand .brand__name{font-size:11px}
  .coupon__title{position:absolute;left:33px;top:58px;font-family:"Oswald",sans-serif;font-weight:600;font-size:46px;line-height:1;color:var(--teal);
    letter-spacing:-1px;transform:scaleX(.74);transform-origin:left top;white-space:nowrap}
  .coupon__web{position:absolute;left:35px;top:108px;color:var(--olive);font-weight:700;font-size:10px}
  .coupon__tag{position:absolute;left:206px;top:22px;width:128px;height:99px}
  .coupon__value{position:absolute;left:237px;top:41px;font-family:"Oswald",sans-serif;font-weight:600;font-size:44px;color:var(--white);letter-spacing:-1px}
  .coupon__offer{position:absolute;left:329px;top:17px;width:179px;height:110px;background:var(--teal);border-radius:6px;
    color:var(--white);padding:16px 0 0 14px;font-family:"Montserrat",sans-serif}
  .coupon__offer b{display:block;font-size:32px;font-weight:800;line-height:32px}
  .coupon__offer span{display:block;font-size:19px;font-weight:700;line-height:19px;margin-top:4px}
</style>
</head>
<body>

<section class="side side--front">
  <div class="brand">
    <span class="brand__mark"></span>
    <span class="brand__name">Energieberatung Wendel</span>
  </div>

  <div class="hero" role="img" aria-label="Foto: Hände halten ein Hausmodell vor einer sonnigen Hügellandschaft mit Wiese und Wald"></div>
  <svg class="hero__corner" viewBox="0 0 537 258" aria-hidden="true">
    <polygon points="537,141 537,258 439,258" fill="var(--teal)"/>
    <polygon points="537,126 537,138 436,258 422,258" fill="var(--white)"/>
  </svg>

  <div class="services">
    <p class="service service--a">Erstellung von Energieausweisen<br>für Vermietung und Verkauf</p>
    <p class="service service--b">Sanierungs- und<br>Modernisierungskonzepte</p>
    <p class="service service--c">Energieberatung</p>
    <p class="service service--d">Fördermittelberatung</p>
  </div>

  <div class="stripes">
    <span style="background:var(--red)"></span>
    <span style="background:var(--orange)"></span>
    <span style="background:var(--yellow)"></span>
  </div>
</section>

<section class="side side--back">
  <div class="intro">
    <p>Wenn Sie Ihre Immobilie verkaufen oder vermieten möchten, ist die Vorlage eines Energieausweises spätestens bei Besichtigung Pflicht. Bei Nichterstellen können Geldbußen ausgesprochen werden.</p>
    <p>Wir unterstützen Sie bei der Erstellung eines Energieausweises, nehmen eine Begutachtung der Gebäudesubstanz vor, zeigen den energetischen IST-Zustand anhand der Energieeffizienzklassen auf und leiten Modernisierungs-empfehlungen zur Verbesserung der Energieeffizienz ab.</p>
    <p>Als Käufer erhalten Sie mit Übergabe des Energieausweises einen Wegweiser, um die Kosten der anstehenden Modernisierung einschätzen zu können und einen Überblick über den baulichen Zustand der Immobilie zu erhalten.</p>
  </div>

  <div class="contact-band">
    <div class="contact-band__name">
      <small>Energieberatung</small>
      <strong>Jonas Wendel</strong>
    </div>
    <div class="contact-band__data">
      <div class="contact-line">
        <svg viewBox="0 0 12 12"><path d="M6 0a4 4 0 0 0-4 4c0 3 4 8 4 8s4-5 4-8a4 4 0 0 0-4-4zm0 5.6A1.6 1.6 0 1 1 6 2.4a1.6 1.6 0 0 1 0 3.2z"/></svg>
        <span>Am Lindenweg 4<br>35410 Talheim</span>
      </div>
      <div class="contact-line">
        <svg viewBox="0 0 12 12"><path d="M2.5 0.5l2 2.5-1.2 1.4c.7 1.6 2 2.9 3.6 3.6L8.3 6.8l2.7 1.9-.8 2.3C5 11 1 7 .6 1.6z"/></svg>
        <span>+49 0151 47203915</span>
      </div>
      <div class="contact-line contact-line--mail">
        <svg viewBox="0 0 12 12"><path d="M0 2.5h12v7H0zM0 2.5l6 4 6-4" stroke="var(--slate)" stroke-width="1"/></svg>
        <span>info@energieberatung-wendel.de</span>
      </div>
    </div>
  </div>

  <div class="cut-line"></div>

  <div class="coupon">
    <div class="coupon__brand">
      <span class="brand__mark"></span>
      <span class="brand__name">Energieberatung Wendel</span>
    </div>
    <div class="coupon__title">GUTSCHEIN</div>
    <div class="coupon__web">www.energieberatung-wendel.de</div>
    <svg class="coupon__tag" viewBox="0 0 128 99" aria-hidden="true">
      <path d="M34 0H128V99H34L0 62V37Z" fill="var(--gold)"/>
      <circle cx="13" cy="49" r="4" fill="var(--white)"/>
    </svg>
    <div class="coupon__value">25.-€</div>
    <div class="coupon__offer">
      <b>RABATT</b>
      <span>für einen<br>Energieausweis</span>
    </div>
  </div>
</section>

</body>
</html>
```